Trade Alert Service needs Youtube thumbnail / channel design

I'm about to set up a Youtube channel which gives real-time trade alerts to earn passive income. I'm looking for a Youtube channel design to include thumbnail and other associated visuals for the channel.
The trade alerts will be focused around selling cash-secured put options on US equities, and directed at people who want investing advice / tips for getting out of the rat race. I'd like the theme to be somewhat serious / credible, without too many eye-popping neon colours like all the other cheap trade alert videos / day trading videos on Youtube. Happy for you to use your experience if you think otherwise though, as you're the designer, not me!

Target Market(s)

Option Traders, Value Investors, People who want passive income

Industry/Entity Type

Finance

Logo Text

Bramblewick Quarter Guild

Requirements
Must have
• All relevant Youtube visuals so that I can upload them to the Youtube channel - all visuals required by Youtube Studio upload within the channel creation page.
A logo so that I can append it to Powerpoint presentations
Nice to have
• A blank Powerpoint slide template showing the logo would be great in chosen colour scheme

```html
<!DOCTYPE html>
<html lang="en">
<head>
<meta charset="utf-8">
<title>Bramblewick Quarter Guild – Thumbnail</title>
<link href="https://fonts.googleapis.com/css2?family=Anton&family=Poppins:wght@600&display=swap" rel="stylesheet">
<style>
  :root {
    --page-bg: #e6e6e6;
    --green-deep: #0e2609;
    --green-mid: #1f6a12;
    --green-bright: #2f9f45;
    --money-light: #8fc58a;
    --money-dark: #4f8f4c;
    --photo-dark: #23282c;
    --photo-light: #3a4046;
    --white: #ffffff;
  }
  html, body {
    margin: 0;
    width: 1200px;
    height: 1200px;
    overflow: hidden;
    background: var(--page-bg);
  }
  .thumbnail {
    position: absolute;
    left: 135px;
    top: 340px;
    width: 929px;
    height: 522px;
    overflow: hidden;
    box-shadow: 0 2px 8px rgba(0,0,0,0.25);
  }
  .thumbnail svg { display: block; }
  .headline { font-family: "Anton", "Impact", sans-serif; }
  .social-name {
    font-family: "Poppins", "Arial", sans-serif;
    font-weight: 600;
    font-size: 12px;
    fill: var(--white);
  }
</style>
</head>
<body>
<div class="thumbnail">
  <svg width="929" height="522" viewBox="0 0 929 522" xmlns="http://www.w3.org/2000/svg">
    <defs>
      <radialGradient id="panel-glow" cx="0.45" cy="0.3" r="0.8">
        <stop offset="0" stop-color="#1f6a12"/>
        <stop offset="1" stop-color="#0e2609"/>
      </radialGradient>
      <linearGradient id="money-tone" x1="0" y1="0" x2="1" y2="1">
        <stop offset="0" stop-color="#4f8f4c"/>
        <stop offset="0.5" stop-color="#8fc58a"/>
        <stop offset="1" stop-color="#4f8f4c"/>
      </linearGradient>
      <linearGradient id="money-fade" x1="0" y1="0" x2="1" y2="0">
        <stop offset="0" stop-color="#1f6a12" stop-opacity="1"/>
        <stop offset="1" stop-color="#1f6a12" stop-opacity="0"/>
      </linearGradient>
      <linearGradient id="photo-tone" x1="0" y1="0" x2="0" y2="1">
        <stop offset="0" stop-color="#3a4046"/>
        <stop offset="1" stop-color="#23282c"/>
      </linearGradient>
    </defs>

    <!-- backgrounds -->
    <rect class="panel-dark" width="929" height="522" fill="url(#panel-glow)"/>
    <rect class="money-backdrop" x="450" width="479" height="522" fill="url(#money-tone)"
          role="img" aria-label="Scattered hundred-dollar banknotes"/>
    <rect class="money-blend" x="420" width="120" height="522" fill="url(#money-fade)"/>

    <!-- presenter photo area -->
    <rect class="presenter-photo" x="520" y="22" width="345" height="510" rx="14"
          fill="url(#photo-tone)" stroke="var(--white)" stroke-width="4"
          role="img" aria-label="Photo of the presenter in a dark suit and white shirt, seated"/>

    <!-- headline -->
    <text class="headline" x="41" y="165" font-size="80" fill="var(--white)"
          textLength="409" lengthAdjust="spacingAndGlyphs">BRAMBLEWICK</text>
    <text class="headline" x="41" y="286" font-size="132" fill="none"
          stroke="var(--white)" stroke-width="3"
          textLength="418" lengthAdjust="spacingAndGlyphs">QUARTER</text>
    <rect class="headline-band" x="41" y="301" width="414" height="122" fill="var(--green-bright)"/>
    <text class="headline" x="64" y="410" font-size="116" fill="var(--white)"
          textLength="372" lengthAdjust="spacingAndGlyphs">GUILD</text>

    <!-- social row -->
    <g class="social-row">
      <circle cx="47" cy="459" r="6" fill="var(--white)"/>
      <text class="social-name" x="57" y="463.5">Ledgerly</text>
      <circle cx="123" cy="459" r="6" fill="var(--white)"/>
      <text class="social-name" x="133" y="463.5">Tickerly</text>
      <circle cx="197" cy="459" r="6" fill="var(--white)"/>
      <text class="social-name" x="207" y="463.5">Putwise</text>
      <line class="social-rule" x1="268" y1="458" x2="515" y2="458" stroke="var(--white)" stroke-width="1.5"/>
    </g>
  </svg>
</div>
</body>
</html>
```